BEACON CABS

Taxi card design

Need changes very slow in replying to my messages.

Target Market(s)

Customers

Industry/Entity Type

Taxi

Contact Information for Business Card

See previous design

Font styles to use
Sans Serif

Colors
A7469A
B969AE
D3A5CF
EDDBEB
F8F0F9
6B429C
8869AF
B7A5CE
E3DAEB
F3F0F8

Requirements
Nice to have
• We are in the business of looking after people, not just driving vehicles front
Should not have
• Front number 01632 480 480 needs to big big

```html
<!DOCTYPE html>
<html lang="en">
<head>
<meta charset="utf-8">
<title>Beacon Cabs – Business Card</title>
<link rel="stylesheet" href="https://fonts.googleapis.com/css2?family=Arimo:wght@400;700&display=swap">
<style>
  :root {
    --bg: #b4b4b4;
    --pink: #e43bb4;
    --magenta: #c6379a;
    --purple: #5d3ba8;
    --violet: #8a45ae;
    --ink: #1b1b1b;
    --grey: #6b6b6b;
    --white: #ffffff;
  }
  * { margin: 0; padding: 0; box-sizing: border-box; }
  html, body { width: 1200px; height: 876px; overflow: hidden; }
  body {
    background: var(--bg);
    font-family: "Arimo", Arial, sans-serif;
    position: relative;
  }
  .card {
    position: absolute;
    top: 284px;
    width: 540px;
    height: 309px;
    border-radius: 3px;
    overflow: hidden;
    box-shadow: 0 10px 24px rgba(0,0,0,.25);
  }
  /* back: contact side */
  .card--contact { left: 40px; background: var(--white); }
  .card--contact .brand {
    position: absolute; left: 150px; top: 36px;
    font-size: 34px; font-weight: 700; color: var(--magenta);
    letter-spacing: .5px;
  }
  .contact-list {
    position: absolute; left: 30px; top: 110px;
    list-style: none; font-size: 13px; color: var(--grey); line-height: 19px;
  }
  .contact-list li { display: flex; align-items: center; gap: 7px; }
  .contact-list svg { width: 11px; height: 11px; flex: none; }
  .phones {
    position: absolute; left: 318px; top: 92px;
    list-style: none; color: var(--grey); font-size: 16px; line-height: 20px;
  }
  .phones li { display: flex; align-items: center; gap: 8px; }
  .phones svg { width: 12px; height: 12px; flex: none; }
  .phones .phone--main { font-size: 23px; font-weight: 700; color: var(--magenta); line-height: 30px; }
  .address {
    position: absolute; left: 300px; top: 190px;
    font-style: normal; font-size: 15px; line-height: 19px; color: var(--grey);
  }
  .edge-band { position: absolute; left: 0; bottom: 0; width: 540px; height: 70px; }
  .service-tag {
    position: absolute; left: 230px; bottom: 14px;
    font-size: 16px; color: var(--white);
  }
  /* front: brand side */
  .card--brand {
    left: 620px;
    background: linear-gradient(125deg, var(--pink) 0%, #b14bb8 45%, var(--purple) 100%);
  }
  .card--brand .brand {
    position: absolute; left: 0; right: 0; top: 112px; text-align: center;
    font-size: 52px; font-weight: 700; color: var(--white); letter-spacing: 1px;
  }
  .services {
    position: absolute; left: 0; right: 0; bottom: 62px; text-align: center;
    font-size: 13px; color: var(--white); letter-spacing: .6px;
  }
</style>
</head>
<body>

<section class="card card--contact" aria-label="Card back with contact details">
  <div class="brand">BEACON CABS</div>

  <ul class="contact-list">
    <li><svg viewBox="0 0 12 12"><path d="M3 1l2 2.5-1.2 1.3a7 7 0 003.4 3.4L8.5 7 11 9l-1 2C5 11 1 7 1 2z" fill="var(--violet)"/></svg>0800 555 0 111</li>
    <li><svg viewBox="0 0 12 12"><rect x="1" y="2.5" width="10" height="7" fill="none" stroke="var(--violet)"/><path d="M1 2.5l5 4 5-4" fill="none" stroke="var(--violet)"/></svg>beaconcabs@mailbox.example</li>
    <li><svg viewBox="0 0 12 12"><circle cx="6" cy="6" r="5" fill="var(--violet)"/><path d="M1 6h10M6 1v10" stroke="#fff" stroke-width=".8"/></svg>www.beaconcabs.example</li>
  </ul>

  <ul class="phones">
    <li class="phone--main"><svg viewBox="0 0 12 12"><path d="M3 1l2 2.5-1.2 1.3a7 7 0 003.4 3.4L8.5 7 11 9l-1 2C5 11 1 7 1 2z" fill="var(--magenta)"/></svg>01632 480 480</li>
    <li><svg viewBox="0 0 12 12"><path d="M3 1l2 2.5-1.2 1.3a7 7 0 003.4 3.4L8.5 7 11 9l-1 2C5 11 1 7 1 2z" fill="var(--magenta)"/></svg>01632 96 06 66</li>
    <li><svg viewBox="0 0 12 12"><path d="M3 1l2 2.5-1.2 1.3a7 7 0 003.4 3.4L8.5 7 11 9l-1 2C5 11 1 7 1 2z" fill="var(--magenta)"/></svg>01632 20 20 21</li>
    <li><svg viewBox="0 0 12 12"><path d="M3 1l2 2.5-1.2 1.3a7 7 0 003.4 3.4L8.5 7 11 9l-1 2C5 11 1 7 1 2z" fill="var(--magenta)"/></svg>0163296 88 11</li>
  </ul>

  <address class="address">St Marks Church Hall<br>Market Row<br>Hollowby HB23 2JE</address>

  <svg class="edge-band" viewBox="0 0 540 70" aria-hidden="true">
    <defs>
      <linearGradient id="band" x1="0" x2="1" y1="0" y2="0">
        <stop offset="0" stop-color="var(--pink)"/>
        <stop offset="1" stop-color="var(--purple)"/>
      </linearGradient>
    </defs>
    <polygon points="0,54 190,54 212,30 540,30 540,70 0,70" fill="var(--ink)"/>
    <polygon points="0,60 194,60 216,36 540,36 540,70 0,70" fill="url(#band)"/>
  </svg>
  <div class="service-tag">24/7 service</div>
</section>

<section class="card card--brand" aria-label="Card front with brand name">
  <div class="brand">BEACON CABS</div>
  <p class="services">• AIRPORT TRANSFERS • MINIBUSES • SCHOOL TRANSPORT</p>
</section>

</body>
</html>
```